Best local air conditioning and heating contractor

We need a website design for a new company in Tampa Bay called the Summit Breeze Cooling Company. We provide superior services for residential and commercial properties as well as maintenance and installing HVAC systems. We also want to sell equipment, parts and filter on the website as well. We want it easy to use for customers. Rich with content and keywords for our area.

Target Market(s)

homeowners in Tampa Bay

Industry/Entity Type

HVAC air conditioning and heating

Coding

Coded - Design and coding required

Number of Pages Required

5+ page

Font styles to use
Sans Serif

Requirements
Nice to have
• would like the colors to be same as logo

```html
<!DOCTYPE html>
<html lang="en">
<head>
<meta charset="utf-8">
<title>Summit Breeze Cooling Company</title>
<link href="https://fonts.googleapis.com/css2?family=Montserrat:wght@400;500;600;700&display=swap" rel="stylesheet">
<style>
:root{
  --red:#e00a0a;
  --red-dark:#b5121b;
  --navy:#14238f;
  --blue:#1a2aa0;
  --ink:#1d1d1d;
  --text:#4a4a4a;
  --soft:#f4f6fb;
  --white:#ffffff;
}
*{margin:0;padding:0;box-sizing:border-box}
html,body{width:1200px;height:3512px;overflow:hidden}
body{font-family:'Montserrat',sans-serif;color:var(--ink);background:var(--white);position:relative}
.abs{position:absolute}
.btn{position:absolute;display:flex;align-items:center;justify-content:center;background:linear-gradient(100deg,var(--red) 75%,var(--red-dark) 75%);color:var(--white);font-size:15px;font-weight:500;border-radius:3px}
.learn{color:var(--red);font-size:16px;font-weight:500;display:flex;align-items:center;gap:8px}
.photo{position:absolute}
.hero{position:absolute;left:0;top:0;width:1200px;height:667px;overflow:hidden}
.hero .scene{position:absolute;inset:0;background:linear-gradient(120deg,#8a4a4e 0%,#6a7a96 55%,#3d5f9a 100%)}
.hero .tint-red{position:absolute;inset:0;background:linear-gradient(180deg,rgba(200,60,60,.85),rgba(165,40,45,.9));clip-path:polygon(0 0,600px 0,780px 667px,0 667px)}
.hero .tint-blue{position:absolute;inset:0;background:rgba(30,45,160,.55);clip-path:polygon(600px 0,1200px 0,1200px 667px,780px 667px)}
.hero h1{position:absolute;left:112px;top:232px;color:var(--white);font-weight:700;font-size:52px;line-height:64px;letter-spacing:1px}
.hero h1 .thin{display:block;font-weight:400;font-size:41px;margin-bottom:10px}
.hero p{position:absolute;left:112px;top:452px;width:520px;color:var(--white);font-size:16px;line-height:26px}
.header{position:absolute;left:112px;top:26px;width:977px;height:110px;background:var(--white);border-radius:10px;overflow:hidden;box-shadow:0 4px 14px rgba(0,0,0,.12)}
.brand{position:absolute;left:24px;top:36px;display:flex;align-items:center;gap:8px;color:var(--navy);font-weight:700;font-size:16px;line-height:19px;width:190px}
.brand .mark{width:14px;height:14px;background:var(--red);flex:none}
.topbar{position:absolute;left:233px;top:0;right:0;height:38px;background:var(--navy);color:var(--white);font-size:14px;display:flex;align-items:center;justify-content:space-between;padding:0 28px 0 26px}
.topbar span{display:flex;align-items:center;gap:6px}
.nav{position:absolute;left:256px;top:66px;display:flex;gap:26px;font-size:15px;color:#333}
.quote{left:823px;top:55px;width:124px;height:40px}
.kicker{position:absolute;font-weight:700;font-size:38px;color:var(--red);letter-spacing:.5px}
.about-frame{left:215px;top:732px;width:408px;height:480px;background:var(--navy)}
.sub{position:absolute;left:674px;top:852px;width:415px;font-size:22px;line-height:34px;font-weight:500;text-align:justify;text-align-last:justify}
.para{position:absolute;font-size:16px;line-height:26px;color:var(--text)}
.check{position:absolute;left:674px;display:flex;gap:14px;width:415px;font-size:16px;line-height:26px;color:var(--text)}
.check svg{flex:none;margin-top:6px}
.services-bg{left:0;top:1302px;width:1200px;height:706px;background:var(--soft)}
.card-cap{position:absolute;background:var(--white);padding:14px 20px 0 24px;height:80px}
.card-cap h3{font-size:17px;font-weight:600;color:var(--navy);margin-bottom:6px;white-space:nowrap}
.products{left:0;top:2008px;width:1200px;height:543px;background:linear-gradient(90deg,#1a2aa0,#2436b0 60%,#1a2aa0)}
.plist{position:absolute;left:112px;display:flex;gap:14px;align-items:center;color:var(--white);font-size:16px;font-weight:600}
.blog h4{font-size:18px;font-weight:600;color:var(--navy);line-height:26px;text-align:justify}
.date{position:absolute;font-size:16px;font-weight:500}
.btxt{position:absolute;font-size:14.5px;line-height:21px;color:var(--text);text-align:justify}
.footer{left:0;top:3260px;width:1200px;height:252px;background:radial-gradient(circle at 1000px 0,#d00d0d 0,#d00d0d 300px,var(--red) 301px)}
.fnav{position:absolute;left:0;width:1200px;top:3418px;display:flex;justify-content:center;gap:35px;color:var(--white);font-size:19px;font-weight:500}
</style>
</head>
<body>

<section class="hero">
  <div class="scene" role="img" aria-label="Technician in a yellow hard hat servicing a wall-mounted air conditioner"></div>
  <div class="tint-red"></div>
  <div class="tint-blue"></div>
  <h1><span class="thin">THE SUMMIT BREEZE</span>COOLING<br>COMPANY</h1>
  <p>Lorem ipsum dolor sit amet, consectetur adipiscing elit, sed do eiusmod tempor incididunt ut labore et dolore magna aliqua. Quis ipsum suspendisse ultrices gravida.</p>
</section>

<header class="header">
  <div class="brand"><span class="mark"></span>Summit Breeze Cooling Company</div>
  <div class="topbar">
    <span><svg width="11" height="14" viewBox="0 0 11 14"><path d="M5.5 0A5.5 5.5 0 0 0 0 5.5C0 9.5 5.5 14 5.5 14S11 9.5 11 5.5A5.5 5.5 0 0 0 5.5 0z" fill="#fff"/></svg>Sed ut perspiciatis unde omni</span>
    <span><svg width="13" height="13" viewBox="0 0 14 14"><circle cx="7" cy="7" r="7" fill="#fff"/><path d="M7 3v4l3 2" stroke="#14238f" stroke-width="1.6" fill="none"/></svg>Mon-Sat: 8am - 5pm</span>
    <span><svg width="13" height="13" viewBox="0 0 24 24"><path d="M6.6 10.8a15 15 0 0 0 6.6 6.6l2.2-2.2a1 1 0 0 1 1-.25 11.4 11.4 0 0 0 3.6.6 1 1 0 0 1 1 1V20a1 1 0 0 1-1 1A17 17 0 0 1 3 4a1 1 0 0 1 1-1h3.5a1 1 0 0 1 1 1c0 1.25.2 2.45.6 3.6a1 1 0 0 1-.25 1z" fill="#fff"/></svg>+1 888 8888 8888</span>
  </div>
  <nav class="nav"><span>Home</span><span>About</span><span>Services</span><span>Products</span><span>Contact Us</span></nav>
  <div class="btn quote">Get A Quote</div>
</header>

<div class="abs about-frame"></div>
<div class="photo" style="left:112px;top:757px;width:483px;height:430px;background:linear-gradient(160deg,#eeeeec,#d9d8d2 60%,#d8cf4a 85%)" role="img" aria-label="Happy couple on a yellow sofa beneath a wall air conditioner"></div>
<h2 class="kicker" style="left:674px;top:795px">ABOUT US</h2>
<p class="sub">Lorem ipsum dolor sit amet, consec<br>tetur adipiscing elit, sed do</p>
<p class="para" style="left:674px;top:925px;width:415px;text-align:justify">Lorem ipsum dolor sit amet, consectetur adipiscing elit, sed do eiusmod tempor incididunt ut labore et dolore magna aliqua. Quis ipsum suspendisse ultrices gravida.</p>
<div class="check" style="top:1049px"><svg width="19" height="19" viewBox="0 0 20 20"><circle cx="10" cy="10" r="10" fill="#14238f"/><path d="M5.5 10.5l3 3 6-6" stroke="#fff" stroke-width="2" fill="none"/></svg><span>Lorem ipsum dolor sit amet, consectetur adipi elit, sed do eiusmod tempor incididunt ut</span></div>
<div class="check" style="top:1109px"><svg width="19" height="19" viewBox="0 0 20 20"><circle cx="10" cy="10" r="10" fill="#14238f"/><path d="M5.5 10.5l3 3 6-6" stroke="#fff" stroke-width="2" fill="none"/></svg><span>Lorem ipsum dolor sit amet, consectetur adipi elit, sed do eiusmod tempor incididunt ut</span></div>
<div class="btn" style="left:674px;top:1177px;width:125px;height:40px">Learn More</div>

<div class="abs services-bg"></div>
<h2 class="kicker" style="left:0;width:1200px;text-align:center;top:1452px">OUR SERVICES</h2>

<div class="photo" style="left:112px;top:1534px;width:299px;height:264px;background:linear-gradient(135deg,#f2f2f0,#c9c7c2 55%,#283c8c)" role="img" aria-label="Technician cleaning an indoor air conditioning unit"></div>
<div class="card-cap" style="left:154px;top:1769px;width:257px"><h3>Maintenance</h3><span class="learn">Learn More <svg width="16" height="10" viewBox="0 0 16 10"><path d="M0 5h14M10 1l4 4-4 4" stroke="#e00a0a" stroke-width="2" fill="none"/></svg></span></div>

<div class="photo" style="left:450px;top:1534px;width:299px;height:264px;background:linear-gradient(135deg,#e8e8e8,#cfd2da 50%,#2a4bb0)" role="img" aria-label="Installer fitting an air conditioner on a brick wall"></div>
<div class="card-cap" style="left:492px;top:1769px;width:257px"><h3>Installing HVAC Systems</h3><span class="learn">Learn More <svg width="16" height="10" viewBox="0 0 16 10"><path d="M0 5h14M10 1l4 4-4 4" stroke="#e00a0a" stroke-width="2" fill="none"/></svg></span></div>

<div class="photo" style="left:790px;top:1534px;width:299px;height:264px;background:linear-gradient(135deg,#f0f0f0,#b9bcc4 50%,#2a40c0)" role="img" aria-label="Gloved hands repairing an air conditioner with a screwdriver"></div>
<div class="card-cap" style="left:832px;top:1769px;width:257px"><h3>Repair Services</h3><span class="learn">Learn More <svg width="16" height="10" viewBox="0 0 16 10"><path d="M0 5h14M10 1l4 4-4 4" stroke="#e00a0a" stroke-width="2" fill="none"/></svg></span></div>

<div class="btn" style="left:503px;top:1881px;width:194px;height:41px">View All Services</div>

<div class="abs products" role="img" aria-label="Blue-toned living room interior"></div>
<h2 class="kicker" style="left:112px;top:2162px;color:var(--white)">OUR PRODUCTS</h2>
<p class="para" style="left:112px;top:2227px;width:600px;color:var(--white)">Lorem ipsum dolor sit amet, consectetur adipiscing elit, sed do eiusmod tempor incididunt ut labore et dolore magna aliqua.</p>
<div class="plist" style="top:2297px"><svg width="19" height="19" viewBox="0 0 20 20"><circle cx="10" cy="10" r="10" fill="#fff"/><path d="M5.5 10.5l3 3 6-6" stroke="#1a2aa0" stroke-width="2" fill="none"/></svg>Air Conditioning Equipment</div>
<div class="plist" style="top:2331px"><svg width="19" height="19" viewBox="0 0 20 20"><circle cx="10" cy="10" r="10" fill="#fff"/><path d="M5.5 10.5l3 3 6-6" stroke="#1a2aa0" stroke-width="2" fill="none"/></svg>Air Conditioning&nbsp; Parts</div>
<div class="plist" style="top:2365px"><svg width="19" height="19" viewBox="0 0 20 20"><circle cx="10" cy="10" r="10" fill="#fff"/><path d="M5.5 10.5l3 3 6-6" stroke="#1a2aa0" stroke-width="2" fill="none"/></svg>Air Conditioning Filters</div>
<div class="btn" style="left:112px;top:2422px;width:177px;height:41px">View All Products</div>
<div class="photo" style="left:750px;top:2189px;width:339px;height:177px;background:linear-gradient(170deg,#ffffff,#e3e6ee 60%,#b9c0d4);border-radius:10px 10px 30px 30px;transform:skewY(-6deg)" role="img" aria-label="White split air conditioner unit"></div>

<h2 class="kicker" style="left:0;width:1200px;text-align:center;top:2697px">OUR LATEST BLOG</h2>

<div class="photo" style="left:112px;top:2785px;width:304px;height:194px;background:linear-gradient(180deg,#f3f3f1,#e2e1dc 60%,#6b6e6a)" role="img" aria-label="Person relaxing on a sofa under an air conditioner"></div>
<div class="date" style="left:109px;top:2993px">May 03, 2024</div>
<div class="blog abs" style="left:112px;top:3027px;width:304px"><h4>Lorem ipsum dolor sit amet, con sectetur adipiscing</h4></div>
<p class="btxt" style="left:112px;top:3090px;width:304px">Lorem ipsum dolor sit amet, consectetur adipiscing elit, sed do eiusmod tempor in cididunt ut labore</p>
<span class="learn abs" style="left:109px;top:3157px">Learn More <svg width="16" height="10" viewBox="0 0 16 10"><path d="M0 5h14M10 1l4 4-4 4" stroke="#e00a0a" stroke-width="2" fill="none"/></svg></span>

<div class="photo" style="left:449px;top:2785px;width:302px;height:194px;background:linear-gradient(135deg,#9fb6c6,#c8d0d6 50%,#1f2b55)" role="img" aria-label="Technician checking outdoor condenser units with gauges"></div>
<div class="date" style="left:446px;top:2993px">May 03, 2024</div>
<div class="blog abs" style="left:449px;top:3027px;width:302px"><h4>Lorem ipsum dolor sit amet, con sectetur adipiscing</h4></div>
<p class="btxt" style="left:449px;top:3090px;width:302px">Lorem ipsum dolor sit amet, consectetur adipiscing elit, sed do eiusmod tempor in cididunt ut labore</p>
<span class="learn abs" style="left:446px;top:3157px">Learn More <svg width="16" height="10" viewBox="0 0 16 10"><path d="M0 5h14M10 1l4 4-4 4" stroke="#e00a0a" stroke-width="2" fill="none"/></svg></span>

<div class="photo" style="left:786px;top:2785px;width:304px;height:194px;background:linear-gradient(180deg,#f4f4f2,#e0dfda 60%,#5e6462)" role="img" aria-label="Person resting on a grey sofa in a cool room"></div>
<div class="date" style="left:783px;top:2993px">May 03, 2024</div>
<div class="blog abs" style="left:786px;top:3027px;width:304px"><h4>Lorem ipsum dolor sit amet, con sectetur adipiscing</h4></div>
<p class="btxt" style="left:786px;top:3090px;width:304px">Lorem ipsum dolor sit amet, consectetur adipiscing elit, sed do eiusmod tempor in cididunt ut labore</p>
<span class="learn abs" style="left:783px;top:3157px">Learn More <svg width="16" height="10" viewBox="0 0 16 10"><path d="M0 5h14M10 1l4 4-4 4" stroke="#e00a0a" stroke-width="2" fill="none"/></svg></span>

<footer class="abs footer"></footer>
<div class="abs" style="left:0;width:1200px;top:3336px;display:flex;justify-content:center;align-items:center;gap:10px;color:var(--white);font-weight:700;font-size:22px">
  <span style="width:16px;height:16px;background:#fff;display:inline-block"></span>Summit Breeze Cooling Company
</div>
<nav class="fnav"><span>Home</span><span>About</span><span>Services</span><span>Products</span><span>Contact Us</span></nav>
<div class="abs" style="left:112px;top:3463px;width:977px;height:1px;background:rgba(255,255,255,.8)"></div>
<p class="abs" style="left:0;width:1200px;top:3478px;text-align:center;color:var(--white);font-size:14.5px">Copyright 2024 The Summit Breeze Cooling Company. All Rights Reserved.</p>

</body>
</html>
```